ALL TEXT Social Media Graphics

We are looking for a series of social media graphics for Instagram (new size: 4:5 (1080 x 1350 pixels) ratio that are ALL TEXT. We want the following quotes below on each graphic; one quote per graphic. AND, In very small letters at the bottom of each graphic, add @PaulaWrenLive
The look and feel of these graphics should be complimentary to the color palette attached below; but keep them simple. But the design is up to you; at the end of this document, I provided various samples of all text graphics that I like as examples.
The Quotes are in the attached WORD document
women trying to lose weight

```html
<!DOCTYPE html>
<html lang="en">
<head>
<meta charset="utf-8">
<title>Summer Reset – Text Posts</title>
<link rel="stylesheet" href="https://fonts.googleapis.com/css2?family=Exo+2:ital,wght@1,300;1,400;1,800;1,900&family=Roboto:ital,wght@0,400;0,700;1,300;1,400;1,700;1,900&display=swap">
<style>
  :root {
    --stage: #ab1553;
    --berry: #a6164f;
    --berry-deep: #8f1043;
    --rose: #ef6b9a;
    --blush: #fbe3ec;
    --blush-soft: #fdf1f5;
    --ink: #111111;
    --grey: #6a6a6a;
    --forest: #1f4a1c;
    --white: #ffffff;
  }
  * { box-sizing: border-box; margin: 0; padding: 0; }
  html, body { width: 1200px; height: 1200px; overflow: hidden; }
  body { background: var(--stage); font-family: "Roboto", Arial, sans-serif; }
  .board { position: relative; width: 1200px; height: 1200px; }

  .post {
    position: absolute; width: 351px; height: 439px; overflow: hidden;
    background: var(--white);
    box-shadow: 0 10px 22px rgba(60, 0, 25, 0.28);
  }
  .post--goal { left: 42px; top: 142px; background: linear-gradient(180deg, #fff 0%, #fdf0f5 55%, #fbdce8 88%, #f7bfd5 100%); }
  .post--weeks { left: 424px; top: 142px; }
  .post--together { left: 806px; top: 142px; background: radial-gradient(ellipse at 30% 20%, #fff 0%, var(--blush-soft) 50%, var(--blush) 100%); }
  .post--snatched { left: 42px; top: 618px; background: radial-gradient(ellipse at 70% 30%, #fff 0%, var(--blush-soft) 55%, var(--blush) 100%); }
  .post--sis { left: 424px; top: 618px; background: radial-gradient(ellipse at 60% 25%, var(--blush) 0%, var(--blush-soft) 55%, #fff 100%); }
  .post--blueprint { left: 806px; top: 618px; }

  .copy { position: absolute; text-transform: uppercase; font-style: italic; }
  .b { font-weight: 700; }
  .berry { color: var(--berry); }
  .rose { color: var(--rose); }

  .handle { position: absolute; right: 22px; bottom: 22px; font-size: 11px; letter-spacing: 0.4px; text-transform: uppercase; color: var(--berry); }

  /* Post 1 */
  .post--goal .copy { left: 60px; top: 97px; text-transform: none; font-family: "Exo 2", Arial, sans-serif; color: var(--forest); font-size: 21px; line-height: 26px; font-weight: 300; }
  .post--goal .big { font-weight: 900; color: var(--berry); font-size: 23px; text-transform: uppercase; letter-spacing: 0.5px; }
  .post--goal .rule { position: absolute; left: 60px; top: 263px; width: 120px; height: 2px; background: #f4c4d6; }
  .post--goal .cta { position: absolute; left: 60px; top: 278px; font-family: "Roboto", Arial, sans-serif; font-style: italic; font-size: 15px; line-height: 22px; color: var(--berry); }
  .post--goal .cta strong { color: var(--ink); font-weight: 900; }
  .post--goal .handle { font-family: "Exo 2", Arial, sans-serif; text-transform: none; font-style: italic; font-weight: 800; color: var(--forest); font-size: 12px; }

  /* Post 2 */
  .post--weeks .copy { left: 26px; top: 60px; font-size: 22px; line-height: 27px; font-weight: 300; color: var(--ink); letter-spacing: 0.3px; }
  .post--weeks .handle { color: var(--ink); font-weight: 700; font-size: 12px; }

  /* Post 3 */
  .post--together .title { position: absolute; left: 42px; top: 38px; font-size: 32px; line-height: 33px; font-weight: 900; font-style: italic; text-transform: uppercase; color: var(--berry); letter-spacing: 0.3px; }
  .post--together .copy { left: 42px; top: 178px; font-size: 20px; line-height: 24px; font-weight: 300; color: var(--grey); }
  .post--together .rule { position: absolute; left: 42px; top: 292px; width: 150px; height: 3px; background: var(--berry); }
  .post--together .cta { position: absolute; left: 42px; top: 310px; font-size: 15px; line-height: 18px; font-style: italic; font-weight: 300; color: var(--grey); text-transform: uppercase; }

  /* Post 4 */
  .post--snatched .copy { left: 27px; top: 84px; font-size: 22px; line-height: 28px; font-weight: 300; color: var(--ink); letter-spacing: 0.3px; }
  .post--snatched .cta { position: absolute; left: 32px; top: 280px; font-size: 19px; line-height: 23px; font-style: italic; font-weight: 300; text-transform: uppercase; color: var(--ink); }
  .post--snatched .handle { color: var(--rose); }

  /* Post 5 */
  .post--sis .copy { left: 23px; top: 70px; font-size: 31px; line-height: 32px; font-weight: 300; color: var(--berry-deep); }
  .post--sis .copy .b { font-weight: 900; }
  .post--sis .cta { position: absolute; left: 23px; top: 290px; font-size: 18px; line-height: 21px; font-style: italic; font-weight: 300; text-transform: uppercase; color: var(--berry); }
  .post--sis .cta strong { color: var(--ink); font-weight: 700; }

  /* Post 6 */
  .post--blueprint .corners { position: absolute; inset: 0; }
  .post--blueprint .copy { left: 83px; top: 106px; font-style: normal; font-size: 20px; line-height: 25px; font-weight: 400; color: var(--berry); letter-spacing: 0.3px; }
  .post--blueprint .pill { position: absolute; left: 0; top: 310px; width: 162px; height: 58px; background: var(--berry); border-radius: 0 29px 29px 0; padding: 10px 0 0 34px; color: var(--white); font-size: 15px; line-height: 17px; font-style: italic; font-weight: 300; text-transform: uppercase; }
  .post--blueprint .pill strong { font-weight: 700; }
  .post--blueprint .handle { color: var(--white); }
</style>
</head>
<body>
<main class="board">

  <article class="post post--goal">
    <p class="copy">If your goal is a<br><span class="big">Tiny waist,<br>flat belly,</span><br>and<br><span class="big">30 pounds down</span><br>this is the plan.</p>
    <div class="rule"></div>
    <p class="cta"><strong>COMMENT;</strong><br>“<strong style="color:var(--berry)">Summer</strong>” to join the<br><b>Glow Girl Summer Reset!</b></p>
    <p class="handle">@PaulaWrenLive</p>
  </article>

  <article class="post post--weeks">
    <p class="copy">You’ve got <span class="b berry">8 weeks</span><br>and the <span class="b berry">perfect plan</span><br>to <span class="b berry">drop 30 pounds.</span><br><br>Let’s get<br><span class="b berry">snatched this summer</span><br>with the <span class="b berry">glow girl<br>summer reset.</span><br><br>Comment <span class="b berry">“Summer”!</span></p>
    <p class="handle">@PaulaWrenLive</p>
  </article>

  <article class="post post--together">
    <h2 class="title">Let’s lose up<br>to 30 pounds<br>this summer<br>together.</h2>
    <p class="copy">Nothing feels better<br>than seeing that<br>scale drop<br>week after week.</p>
    <div class="rule"></div>
    <p class="cta"><b class="berry">Comment “Summer”</b><br>to join the glow<br>girl summer reset!</p>
    <p class="handle">@PaulaWrenLive</p>
  </article>

  <article class="post post--snatched">
    <p class="copy"><span class="b rose">Snatched waist,<br>flat tummy,</span><br>30 pounds lighter<br>that’s what the <span class="rose">glow<br>girl summer reset</span><br><span class="b rose">challenge delivers.</span></p>
    <p class="cta"><b>Comment;</b><br><b class="berry">“Glow girl”</b> to get<br>the plan</p>
    <p class="handle">@PaulaWrenLive</p>
  </article>

  <article class="post post--sis">
    <p class="copy">Sis,<br>we’re <span class="b">dropping<br>belly flat</span> and<br>saying <span class="b">goodbye</span><br>to <span class="b">stubborn<br>pounds.</span></p>
    <p class="cta"><strong>Comment <span style="color:var(--berry)">“Summer”</span>!</strong><br>to join the glow girl<br>summer reset</p>
    <p class="handle">@PaulaWrenLive</p>
  </article>

  <article class="post post--blueprint">
    <svg class="corners" width="351" height="439" viewBox="0 0 351 439" aria-hidden="true">
      <defs>
        <linearGradient id="cornerTop" x1="0" y1="0" x2="1" y2="1">
          <stop offset="0" stop-color="#a6164f"/>
          <stop offset="1" stop-color="#f3c3d5"/>
        </linearGradient>
        <linearGradient id="cornerBottom" x1="1" y1="1" x2="0" y2="0">
          <stop offset="0" stop-color="#a6164f"/>
          <stop offset="1" stop-color="#f6d0de"/>
        </linearGradient>
      </defs>
      <polygon points="0,0 178,0 0,190" fill="url(#cornerTop)"/>
      <polygon points="351,292 351,439 190,439" fill="url(#cornerBottom)"/>
    </svg>
    <p class="copy">There’s still <b>time<br>to drop</b> the<br><b>30 pounds</b> and<br>slay this summer.<br>The glow girl<br>summer reset<br>has the <b>blueprint.</b></p>
    <p class="pill">Comment;<br><strong>“Glow girl”!</strong></p>
    <p class="handle">@PaulaWrenLive</p>
  </article>

</main>
</body>
</html>
```